Classy, Elegant, Simple Business Card Design

Looking to have a classy, simple, and elegant design. Want a top notch designed business card. I really like the look of the new brivo credit card. I also like the design I attached. I am trying to reach 21-29 year old females for booking us for there wedding or event. We offer Disc Jockey Service, Photo Booth Rentals, and Uplighting .

Target Market(s)

21-28 year old females

Contact Information for Business Card

Has to have logo, website, email, and phone number

Font styles to use
Other font styles liked:
• open to font choice, modern, clean
Designer to choose
33a6d7
0791cd
0555a3
ffffff

Requirements
Must have
• Has to have logo, website, email, and phone number
Nice to have
• I really like the design of the new brivo credit card. I also included my logo and some designs I like
Should not have
• clutter or too much info

```html
<!DOCTYPE html>
<html lang="en">
<head>
<meta charset="utf-8">
<title>Tidelight Event Group – Business Card</title>
<link rel="stylesheet" href="https://fonts.googleapis.com/css2?family=Kaushan+Script&family=Montserrat:wght@400;700&display=swap">
<style>
  :root {
    --navy: #0f3366;
    --navy-deep: #0b2a57;
    --wave-line: #2f6fa8;
    --sky: #33a6d7;
    --blue: #0791cd;
    --royal: #0555a3;
    --ink: #13284d;
    --paper: #ffffff;
    --card-white: #f7f7f5;
    --backdrop: #e8e5e0;
  }
  * { margin: 0; padding: 0; box-sizing: border-box; }
  html, body {
    width: 900px;
    height: 1200px;
    overflow: hidden;
    background: var(--backdrop);
    font-family: "Montserrat", sans-serif;
  }
  .canvas {
    position: relative;
    width: 900px;
    height: 1200px;
  }
  .card {
    position: absolute;
    border-radius: 16px;
    overflow: hidden;
    box-shadow: 0 6px 14px rgba(0, 0, 0, 0.25);
  }

  /* Front */
  .card-front {
    left: 78px;
    top: 137px;
    width: 762px;
    height: 433px;
  }
  .wave-field {
    position: absolute;
    inset: 0;
    background: linear-gradient(135deg, var(--navy-deep) 0%, var(--navy) 50%, #14407a 100%);
  }
  .brand-disc {
    position: absolute;
    left: 205px;
    top: 41px;
    width: 350px;
    height: 350px;
    border-radius: 50%;
    background: var(--paper);
    display: flex;
    flex-direction: column;
    align-items: center;
    justify-content: center;
    color: var(--royal);
    font-weight: 400;
  }
  .brand-name {
    font-size: 36px;
    letter-spacing: 2px;
    line-height: 1;
  }
  .brand-tagline {
    margin-top: 8px;
    font-size: 14px;
    letter-spacing: 6px;
    line-height: 1;
  }

  /* Back */
  .card-back {
    left: 77px;
    top: 630px;
    width: 766px;
    height: 436px;
    background: var(--card-white);
  }
  .person-name {
    position: absolute;
    top: 46px;
    left: 0;
    width: 100%;
    text-align: center;
    font-family: "Kaushan Script", cursive;
    font-size: 82px;
    line-height: 1.2;
  }
  .person-name .first { color: var(--ink); }
  .person-name .last { color: var(--sky); }
  .contact-list {
    position: absolute;
    top: 220px;
    left: 0;
    width: 100%;
    list-style: none;
    text-align: center;
    color: var(--ink);
    font-size: 20px;
    letter-spacing: 1px;
    line-height: 31px;
  }
  .services {
    position: absolute;
    top: 371px;
    left: 0;
    width: 100%;
    text-align: center;
    color: var(--ink);
    font-size: 15px;
    font-weight: 700;
    letter-spacing: 2px;
  }
  .services .divider { margin: 0 8px; font-weight: 400; }
</style>
</head>
<body>
  <main class="canvas">
    <section class="card card-front">
      <div class="wave-field" role="img" aria-label="Navy background with fine flowing wave lines"></div>
      <div class="brand-disc">
        <span class="brand-name">TIDELIGHT</span>
        <span class="brand-tagline">EVENT GROUP</span>
      </div>
    </section>

    <section class="card card-back">
      <h1 class="person-name"><span class="first">Marla</span> <span class="last">Quinn</span></h1>
      <ul class="contact-list">
        <li class="contact-phone">+01 98 765 4320</li>
        <li class="contact-email">HELLO@TIDELIGHTEVENTGROUP.COM</li>
        <li class="contact-web">WWW.TIDELIGHTEVENTGROUP.COM</li>
      </ul>
      <p class="services">DISC JOCKEY SERVICE<span class="divider">|</span>PHOTO BOOTH RENTALS<span class="divider">|</span>UPLIGHTING</p>
    </section>
  </main>
</body>
</html>
```